Need Flyer for Our Real estate Agency

Need to run General Campaign for our agency with Start of New Year as our theme ..Must have an agent's picture on the DL..
Address:
9 / 386Barwin rd, Truganina VIC 3029
Ph:03 9142 7305
email:info@koridanrealestate.example.au
www.koridanrealestate.example.au
Something like as attached picture..
Target Market(s)
Home Buyers
Industry/Entity Type
Real Estate Agent
Requirements
Must have
- Our Logo Colours

```html
<!DOCTYPE html>
<html lang="en">
<head>
<meta charset="utf-8">
<title>Koridan Real Estate – New Year Campaign Banners</title>
<link rel="stylesheet" href="https://fonts.googleapis.com/css2?family=Lato:wght@300;400;700&display=swap">
<style>
  :root {
    --page-bg: #d3d4d6;
    --navy: #0f2257;
    --navy-deep: #0a1842;
    --maroon: #6e1119;
    --white: #ffffff;
    --curve-grey: #e4e6ea;
  }
  * { margin: 0; padding: 0; box-sizing: border-box; }
  html, body {
    width: 1197px; height: 1200px; overflow: hidden;
    background: var(--page-bg);
    font-family: "Lato", sans-serif;
  }
  .banner {
    position: absolute; left: 73px; width: 1060px; height: 504px;
    overflow: hidden;
    box-shadow: 0 6px 10px rgba(0,0,0,0.18);
  }
  .banner--appraisal { top: 56px; }
  .banner--contact { top: 638px; }
  .banner__art { position: absolute; inset: 0; width: 1060px; height: 504px; }
  .brand-name {
    position: absolute; color: var(--white);
    font-weight: 400; font-size: 54px; letter-spacing: 5px;
    transform: translateX(-50%); white-space: nowrap; line-height: 1;
  }
  .banner--appraisal .brand-name { left: 290px; top: 140px; }
  .banner--contact .brand-name { left: 769px; top: 140px; }

  .headline {
    position: absolute; left: 290px; top: 236px; transform: translateX(-50%);
    width: 450px; text-align: center; color: var(--white);
    font-weight: 300; font-size: 35px; line-height: 49px;
  }
  .subline {
    position: absolute; left: 290px; top: 338px; transform: translateX(-50%);
    white-space: nowrap; color: var(--white); font-size: 17px; font-weight: 400;
  }
  .subline strong { font-weight: 700; }
  .call-button {
    position: absolute; left: 92px; top: 408px; width: 399px; height: 50px;
    background: var(--white); border-radius: 25px;
    display: flex; align-items: center; justify-content: center; gap: 8px;
    color: var(--maroon); font-weight: 700; font-size: 22px;
    box-shadow: 0 3px 6px rgba(0,0,0,0.25);
  }
  .call-button svg { width: 22px; height: 22px; }
  .offer-note {
    position: absolute; left: 290px; top: 467px; transform: translateX(-50%);
    color: var(--white); font-size: 19px; font-weight: 300; white-space: nowrap;
  }

  .agent-title {
    position: absolute; left: 608px; top: 242px;
    color: var(--white); font-size: 22px; font-weight: 300;
  }
  .contact-list { position: absolute; left: 608px; top: 282px; list-style: none; }
  .contact-list li {
    display: flex; align-items: center; gap: 12px; height: 40px;
    color: var(--white); font-size: 19px; font-weight: 300;
  }
  .contact-list svg { width: 19px; height: 19px; flex: none; }
  .office-address {
    position: absolute; left: 745px; top: 454px; transform: translateX(-50%);
    color: var(--white); font-size: 20px; font-weight: 300; white-space: nowrap;
  }
</style>
</head>
<body>

<section class="banner banner--appraisal">
  <svg class="banner__art" viewBox="0 0 1060 504">
    <defs>
      <linearGradient id="navyGradA" x1="0" y1="0" x2="1" y2="1">
        <stop offset="0" stop-color="#0d1f52"/>
        <stop offset="0.6" stop-color="#13296a"/>
        <stop offset="1" stop-color="#0a1842"/>
      </linearGradient>
      <linearGradient id="agentPhotoGrad" x1="0" y1="0" x2="0" y2="1">
        <stop offset="0" stop-color="#b9cde3"/>
        <stop offset="0.45" stop-color="#c7b9a2"/>
        <stop offset="0.75" stop-color="#56627a"/>
        <stop offset="1" stop-color="#3d4a63"/>
      </linearGradient>
    </defs>
    <rect class="navy-field" width="1060" height="504" fill="url(#navyGradA)"/>
    <rect class="maroon-band" x="0" y="430" width="680" height="74" fill="var(--maroon)"/>
    <line x1="0" y1="431" x2="680" y2="431" stroke="var(--white)" stroke-width="3"/>
    <path class="curve-accent" d="M627 0 Q560 250 638 504 L668 504 Q590 250 645 0 Z" fill="var(--white)"/>
    <path d="M645 0 Q590 250 668 504 L1060 504 L1060 0 Z" fill="url(#agentPhotoGrad)" role="img" aria-label="Photo of the agent in a suit standing in front of a two-storey family home at dusk"/>
  </svg>
  <div class="brand-name">KORIDAN</div>
  <p class="headline">Curios to know what your home is worth?</p>
  <p class="subline">START THE NEW YEAR WITH <strong>ARJUN MEHTA</strong> AND FIND OUT!</p>
  <div class="call-button">
    <span>CALL ME NOW!</span>
    <svg viewBox="0 0 24 24"><circle cx="12" cy="12" r="10.5" fill="none" stroke="currentColor" stroke-width="2"/><path d="M8.2 6.5l1.8-.3 1.1 2.6-1.2 1a7 7 0 003.3 3.3l1-1.2 2.6 1.1-.3 1.8c-.2.6-.8 1-1.5.9A9 9 0 017.3 8c-.1-.7.3-1.3.9-1.5z" fill="currentColor"/></svg>
    <span>0412 587 930</span>
  </div>
  <p class="offer-note">For Free property Appraisal</p>
</section>

<section class="banner banner--contact">
  <svg class="banner__art" viewBox="0 0 1060 504">
    <defs>
      <linearGradient id="navyGradB" x1="1" y1="0" x2="0" y2="1">
        <stop offset="0" stop-color="#0a1842"/>
        <stop offset="0.5" stop-color="#13296a"/>
        <stop offset="1" stop-color="#0d1f52"/>
      </linearGradient>
      <linearGradient id="handsPhotoGrad" x1="0" y1="0" x2="1" y2="1">
        <stop offset="0" stop-color="#2f4560"/>
        <stop offset="0.45" stop-color="#d9b8a4"/>
        <stop offset="0.6" stop-color="#d9534f"/>
        <stop offset="1" stop-color="#8a9aab"/>
      </linearGradient>
    </defs>
    <rect width="1060" height="504" fill="url(#navyGradB)"/>
    <rect class="maroon-band" x="430" y="432" width="630" height="72" fill="var(--maroon)"/>
    <line x1="430" y1="433" x2="1060" y2="433" stroke="var(--white)" stroke-width="3"/>
    <path class="curve-accent" d="M311 0 L405 0 Q478 220 442 504 L420 504 Q445 200 311 0 Z" fill="var(--curve-grey)"/>
    <path class="curve-accent" d="M311 0 L332 0 Q460 200 432 504 L420 504 Q445 200 311 0 Z" fill="var(--white)"/>
    <path d="M0 0 L311 0 Q445 200 420 504 L0 504 Z" fill="url(#handsPhotoGrad)" role="img" aria-label="Photo of cupped hands protecting a small red model house"/>
  </svg>
  <div class="brand-name">KORIDAN</div>
  <p class="agent-title">Arjun Mehta, Sales Manager</p>
  <ul class="contact-list">
    <li>
      <svg viewBox="0 0 24 24"><circle cx="12" cy="12" r="10.5" fill="none" stroke="#fff" stroke-width="2"/><path d="M8.2 6.5l1.8-.3 1.1 2.6-1.2 1a7 7 0 003.3 3.3l1-1.2 2.6 1.1-.3 1.8c-.2.6-.8 1-1.5.9A9 9 0 017.3 8c-.1-.7.3-1.3.9-1.5z" fill="#fff"/></svg>
      <span>03 9142 7305</span>
    </li>
    <li>
      <svg viewBox="0 0 24 24"><circle cx="12" cy="12" r="10.5" fill="none" stroke="#fff" stroke-width="2"/><rect x="6.5" y="8.5" width="11" height="7.5" fill="none" stroke="#fff" stroke-width="1.6"/><path d="M6.5 8.5l5.5 4.2 5.5-4.2" fill="none" stroke="#fff" stroke-width="1.6"/></svg>
      <span>arjun.mehta@koridanrealestate.example.au</span>
    </li>
    <li>
      <svg viewBox="0 0 24 24"><circle cx="12" cy="12" r="10.5" fill="none" stroke="#fff" stroke-width="2"/><circle cx="12" cy="12" r="6" fill="none" stroke="#fff" stroke-width="1.4"/><ellipse cx="12" cy="12" rx="2.6" ry="6" fill="none" stroke="#fff" stroke-width="1.2"/><path d="M6 12h12" stroke="#fff" stroke-width="1.2"/></svg>
      <span>www.koridanrealestate.example.au</span>
    </li>
  </ul>
  <p class="office-address">9/386 Barwin Rd Elmsbury, Northvale, Australia 4872</p>
</section>

</body>
</html>
```